marlowe charters

We provide boar charter for :Fishing/whale watching and diving in Sydney Harbour providing for 12 passengersI have yet to have web page made but want to make logo first then do web page later. So I want to be able to edit and add this site to card later

Contact Information for Business Card

Captain Glen (Skip) Wigellphone no 0457710098email awigell4@gmail.comCompany name Brightwater Voyages Pty Ltd in association with open reef cruises

Font styles to use
Serif

Requirements
Nice to have
• perhaps a photo of boat and some stick diagrams of fishing.whales and diviving

```html
<!DOCTYPE html>
<html lang="en">
<head>
<meta charset="utf-8">
<title>Marlowe Charters – Business Card</title>
<link rel="stylesheet" href="https://fonts.googleapis.com/css2?family=EB+Garamond:ital,wght@0,400;0,500;1,400&display=swap">
<style>
  :root {
    --card-bg: #ffffff;
    --ink: #111111;
    --ink-soft: #3a3a3a;
    --rule: #1f4f96;
    --sky-top: #e3ecf3;
    --sky-low: #c4d7e8;
    --sea-high: #2c62aa;
    --sea-mid: #1d4f9c;
    --sea-deep: #0f3f8c;
  }
  html, body {
    margin: 0;
    padding: 0;
    overflow: hidden;
    background: var(--card-bg);
  }
  .card {
    position: relative;
    width: 1200px;
    height: 741px;
    background: var(--card-bg);
    overflow: hidden;
    font-family: "EB Garamond", Georgia, serif;
    color: var(--ink);
  }
  .boat-photo {
    position: absolute;
    left: 71px;
    top: 83px;
    width: 484px;
    height: 289px;
    background: linear-gradient(
      to bottom,
      var(--sky-top) 0%,
      var(--sky-low) 11%,
      var(--sea-high) 14%,
      var(--sea-mid) 55%,
      var(--sea-deep) 100%
    );
  }
  .identity {
    position: absolute;
    left: 723px;
    top: 196px;
    width: 440px;
  }
  .business-name {
    margin: 0;
    font-family: "EB Garamond", Georgia, serif;
    font-weight: 500;
    font-size: 52px;
    line-height: 1;
    color: var(--ink);
  }
  .services {
    margin: 12px 0 0;
    font-style: italic;
    font-size: 20px;
    line-height: 1.3;
    color: var(--ink-soft);
  }
  .divider {
    width: 120px;
    height: 2px;
    margin: 22px 0 20px;
    background: var(--rule);
  }
  .contact {
    margin: 0;
    font-style: normal;
    font-size: 20px;
    line-height: 1.45;
  }
  .contact .captain {
    font-weight: 500;
    font-size: 22px;
  }
  .company {
    margin: 18px 0 0;
    font-size: 17px;
    line-height: 1.4;
    color: var(--ink-soft);
  }
</style>
</head>
<body>
  <main class="card">
    <div class="boat-photo" role="img" aria-label="Photo of a white charter boat cruising across deep blue open sea under a pale sky"></div>
    <section class="identity">
      <h1 class="business-name">Marlowe Charters</h1>
      <p class="services">Fishing · Whale Watching · Diving<br>Sydney Harbour · up to 12 passengers</p>
      <div class="divider"></div>
      <address class="contact">
        <div class="captain">Captain Glen (Skip) Ferrant</div>
        <div>Ph 0462 385 147</div>
        <div>gferrant7@tidemail.net</div>
      </address>
      <p class="company">Brightwater Voyages Pty Ltd<br>in association with open reef cruises</p>
    </section>
  </main>
</body>
</html>
```